Kestrel Roofing & Restoration Business Card Design

Lookiing for a double sided business card design that will have rounded corners, will look good with Spot UV, Soft Laminate, or Gloss
Front of card should have Logo, Name and Contact Info, License numbers
Back of card should have Logo, maybe other small details

```html
<!DOCTYPE html>
<html lang="en">
<head>
<meta charset="utf-8">
<title>Kestrel Roofing &amp; Restoration — Business Card</title>
<link rel="stylesheet" href="https://fonts.googleapis.com/css2?family=Open+Sans:wght@400;600;700&display=swap">
<style>
  :root {
    --stage: #151515;
    --card: #1f1f20;
    --blue: #0ea5e4;
    --white: #f2f2f2;
    --silver: #b9b9bb;
  }
  * { margin: 0; padding: 0; box-sizing: border-box; }
  html, body { width: 1200px; height: 977px; overflow: hidden; background: var(--stage); }
  .canvas { position: relative; width: 1200px; height: 977px; }

  .card {
    position: absolute;
    width: 560px; height: 320px;
    background: var(--card);
    border-radius: 22px;
    overflow: hidden;
    font-family: "Open Sans", sans-serif;
    color: var(--white);
  }
  .card--back { left: 60px; top: 90px; }
  .card--front { left: 580px; top: 560px; }

  /* Back: company name */
  .brand {
    position: absolute; inset: 0;
    display: flex; align-items: center; justify-content: center; gap: 12px;
  }
  .brand__square { width: 16px; height: 16px; background: var(--blue); flex: none; }
  .brand__name {
    font-weight: 700; font-size: 26px; letter-spacing: 0.5px;
    color: var(--silver); white-space: nowrap;
  }

  /* Front: person + contact */
  .person { position: absolute; left: 60px; top: 150px; }
  .person__name { font-weight: 700; font-size: 30px; color: var(--blue); letter-spacing: 0.5px; }
  .person__role { font-size: 17px; color: var(--white); margin-top: 2px; }

  .card__rule { position: absolute; left: 300px; top: 60px; width: 2px; height: 150px; background: var(--blue); }

  .contact { position: absolute; left: 322px; top: 48px; font-size: 13px; line-height: 1.45; list-style: none; }
  .contact li { display: flex; gap: 8px; align-items: flex-start; }
  .contact li + li { margin-top: 4px; }
  .contact svg { flex: none; width: 13px; height: 13px; margin-top: 3px; fill: var(--blue); }
  .contact__company { font-weight: 700; }

  .band { position: absolute; left: 0; bottom: 0; width: 560px; height: 70px; }
  .band__url {
    position: absolute; left: 170px; bottom: 16px;
    font-size: 15px; font-weight: 600; letter-spacing: 6px; color: var(--card);
  }
</style>
</head>
<body>
<main class="canvas">

  <section class="card card--back" aria-label="Card back">
    <div class="brand">
      <span class="brand__square"></span>
      <span class="brand__name">Kestrel Roofing &amp; Restoration</span>
    </div>
  </section>

  <section class="card card--front" aria-label="Card front">
    <div class="person">
      <div class="person__name">DANIEL HAYES</div>
      <div class="person__role">Founder &amp; Director</div>
    </div>
    <div class="card__rule"></div>
    <ul class="contact">
      <li>
        <svg viewBox="0 0 12 12"><path d="M6 0a4 4 0 0 0-4 4c0 3 4 8 4 8s4-5 4-8a4 4 0 0 0-4-4zm0 5.5A1.5 1.5 0 1 1 6 2.5a1.5 1.5 0 0 1 0 3z"/></svg>
        <span><span class="contact__company">Kestrel Roofing &amp; Restoration</span><br>418 Harbor Lane, Millbrook<br>State &amp; Country, ZIP Code</span>
      </li>
      <li>
        <svg viewBox="0 0 12 12"><path d="M2.5 0.5l2 2.5-1 1.3a7 7 0 0 0 4.2 4.2L9 7.5l2.5 2-1.2 2C5 11.5 0.5 7 0.5 1.7z"/></svg>
        <span>(555) 014-2290</span>
      </li>
      <li>
        <svg viewBox="0 0 12 12"><path d="M3 0h6a1 1 0 0 1 1 1v10a1 1 0 0 1-1 1H3a1 1 0 0 1-1-1V1a1 1 0 0 1 1-1zm0 1.5v8h6v-8z"/></svg>
        <span>(555) 014-2291</span>
      </li>
      <li>
        <svg viewBox="0 0 12 12"><path d="M3 0h6v3H3zM1 4h10v5H9v3H3V9H1zm3 4v3h4V8z"/></svg>
        <span>(555) 014-2292</span>
      </li>
      <li>
        <svg viewBox="0 0 12 12"><path d="M0 2h12v8H0zm1 1v.4l5 3.3 5-3.3V3z"/></svg>
        <span>info@kestrelroofing.com</span>
      </li>
    </ul>
    <svg class="band" viewBox="0 0 560 70" preserveAspectRatio="none" aria-hidden="true">
      <polygon points="120,8 560,8 560,58 90,58" fill="var(--blue)"/>
    </svg>
    <div class="band__url">WWW.KESTRELROOFING.COM</div>
  </section>

</main>
</body>
</html>
```